meadowbrook cooling & muffler (the key to your automotive needs)

we need a business card design for a company that started out as a radiator shop cleaning repairing recoring or selling new radiators. then we got into fuel tank repair cleaning repairing and lining if the tank leaks we fix it if it has jelled gas or rust we clean it then roll a liner in it no more fuel touching the tank.later we started doing exhaust from small single exhaust to custom duels.now the first of the year we started selling and repairing tires. Now we are doing alignments . we also do brakes and suspension and oil changes we need some way to get the message out about all we do.I would like to see some flare in the writing of the name of the business but still easily read.read. I'm thinking on black and red as colors.but im open for suggestions Id like it to be eye catching and memorable.
Updates

Project Deadline Extended
Reason: i dont have a logo for you please make me one

Target Market(s)

4 wheel alignment-tires new and used.radiator clean and repair recores new complete radiators.fuel tank cleaning and repair and liners.exhaust standard single and custom duels.cars,trucks, and buses.from the youngest driver to the oldest.

Industry/Entity Type

Automotive

Contact Information for Business Card

Meadowbrook Cooling & Muffler Inc. 418 S Pelling road English in.40000 555-204-7183 m-f 9-5 sat 9-12 for tires call 812-365-9497m-f8-5 sat8-12

Font styles to use
Decorative

Colors
000000
ec1f27

Requirements
Must have
• eye catching colors and letters. both phone numbers and hours.logo
Nice to have
• list of things we can do

```html
<!DOCTYPE html>
<html lang="en">
<head>
<meta charset="utf-8">
<title>Meadowbrook Cooling &amp; Muffler Inc — Business Card</title>
<link rel="stylesheet" href="https://fonts.googleapis.com/css2?family=Saira+Semi+Condensed:wght@400;600&display=swap">
<style>
  :root{
    --ink:#000000;
    --brand-red:#ec1f27;
    --paper:#ffffff;
    --paper-shade:#eeeeee;
    --grey-text:#555555;
    --frame:#1a1a1a;
    --stage:#e6e2dc;
  }
  *{box-sizing:border-box;margin:0;padding:0}
  html,body{width:1200px;height:902px;overflow:hidden}
  body{
    background:var(--stage);
    font-family:"Saira Semi Condensed",sans-serif;
    display:flex;align-items:center;justify-content:center;gap:40px;
  }
  .card{
    width:560px;height:320px;position:relative;overflow:hidden;
    background:linear-gradient(160deg,var(--paper),var(--paper-shade));
    box-shadow:0 6px 18px rgba(0,0,0,.25);
  }
  /* front */
  .front-band{position:absolute;inset:0 0 auto 0;height:170px}
  .front-band svg{display:block}
  .brand{position:absolute;display:flex;align-items:center;gap:14px}
  .brand-dot{width:58px;height:58px;border-radius:50%;background:var(--brand-red);flex:none}
  .brand-name{font-weight:600;line-height:.9;letter-spacing:-.5px}
  .brand-sub{font-weight:400;line-height:1.1}
  .front .brand{left:28px;top:28px}
  .front .brand-name{color:var(--paper);font-size:60px}
  .front .brand-sub{color:var(--paper);font-size:24px}
  .photo-row{position:absolute;left:22px;right:22px;bottom:22px;display:flex;gap:12px}
  .photo-frame{flex:1;height:122px;border:4px solid var(--frame);background:var(--paper);padding:6px}
  .photo{width:100%;height:100%}
  .photo--exhaust{background:linear-gradient(135deg,#f4f4f4,#b9b9b9 60%,#e2e2e2)}
  .photo--tires{background:radial-gradient(circle at 50% 55%,#6e6e6e,#9a9a9a 45%,#eeeeee 75%)}
  .photo--radiator{background:linear-gradient(160deg,#d8d8d8,#7b7b7b 55%,#c8c8c8)}
  /* back */
  .back{padding:34px 30px}
  .back .brand{position:static;align-items:flex-start}
  .back .brand-dot{margin-top:22px}
  .back .brand-name{color:var(--ink);font-size:60px}
  .back .brand-sub{color:var(--ink);font-size:24px}
  .services{margin-top:6px;color:var(--grey-text);font-size:17px;letter-spacing:.3px}
  .contact{margin-top:22px;font-size:16px;line-height:1.45;color:var(--ink)}
  .contact .tag{font-size:14px}
  .contact .address{color:var(--grey-text)}
</style>
</head>
<body>

  <section class="card front" aria-label="Card front">
    <div class="front-band">
      <svg width="560" height="170" viewBox="0 0 560 170" aria-hidden="true">
        <polygon points="0,0 560,0 560,120 0,170" fill="var(--ink)"/>
      </svg>
    </div>
    <div class="brand">
      <span class="brand-dot" aria-hidden="true"></span>
      <div>
        <div class="brand-name">Meadowbrook</div>
        <div class="brand-sub">Cooling &amp; Muffler Inc</div>
      </div>
    </div>
    <div class="photo-row">
      <div class="photo-frame"><div class="photo photo--exhaust" role="img" aria-label="Photo of chrome exhaust pipe and muffler"></div></div>
      <div class="photo-frame"><div class="photo photo--tires" role="img" aria-label="Photo of a stack of tires"></div></div>
      <div class="photo-frame"><div class="photo photo--radiator" role="img" aria-label="Photo of a car radiator"></div></div>
    </div>
  </section>

  <section class="card back" aria-label="Card back">
    <div class="brand">
      <span class="brand-dot" aria-hidden="true"></span>
      <div>
        <div class="brand-name">Meadowbrook</div>
        <div class="brand-sub">Cooling &amp; Muffler Inc</div>
        <p class="services">Brakes - suspension - fuel tank repair and liners</p>
      </div>
    </div>
    <div class="contact">
      <p>mon - fri 9 - 5 &nbsp;sat 9 - 12 &nbsp;(555)204-7183 <span class="tag">tire &amp; alignment</span></p>
      <p>mon - fri 8 - 5 &nbsp;sat 8 - 12 &nbsp;(555)204-6251</p>
      <p class="address">418 S Pelling road Harlow ohio</p>
    </div>
  </section>

</body>
</html>
```